Nur Briefpapier und VK für Pflegedienst, Logo vorhanden!!!!
Zielgruppe
Wir sind ein Pflegedienst, unsere Zielgruppe sind Krankenkassen und Patienten und andere Krankenhäuser mit denen wir zusammen arbeiten.
Aufgabenstellung
modern, seriös, elitär

```html
<!DOCTYPE html>
<html lang="de">
<head>
<meta charset="utf-8">
<title>Fenrokare Pflegedienst – Geschäftsausstattung</title>
<link rel="stylesheet" href="https://fonts.googleapis.com/css2?family=Ubuntu:wght@300;400;500;700&display=swap">
<style>
  :root {
    --red-light: #e8262f;
    --red: #e3131f;
    --red-mid: #c8171c;
    --red-dark: #93161a;
    --brand: #a3161a;
    --ink: #333333;
    --grey: #6b6b6b;
    --paper: #ffffff;
    --band: linear-gradient(90deg, var(--red-light) 0%, var(--red) 14%, var(--red-mid) 50%, var(--red-dark) 100%);
    --shadow: 5px 6px 6px rgba(0,0,0,.38);
  }
  * { margin: 0; padding: 0; box-sizing: border-box; }
  html, body { width: 1200px; height: 1200px; overflow: hidden; background: var(--paper); }
  body { position: relative; font-family: "Ubuntu", sans-serif; color: var(--ink); }

  .sheet { position: absolute; box-shadow: var(--shadow); }

  /* Logo stand-in */
  .wordmark { display: flex; flex-direction: column; align-items: center; font-family: "Ubuntu", sans-serif; }
  .wordmark-row { display: flex; align-items: center; gap: 0.3em; font-weight: 700; line-height: 1; }
  .wordmark-square { width: 0.55em; height: 0.55em; background: currentColor; }
  .wordmark-sub { font-weight: 300; line-height: 1; margin-top: 0.4em; }

  /* Business card back */
  .card-back { left: 571px; top: 96px; width: 270px; height: 175px; background: var(--band); border: 1px solid #8a1216; }
  .card-back .wordmark { position: absolute; left: 0; right: 0; top: 66px; color: #fff; }
  .card-back .wordmark-row { font-size: 19px; }
  .card-back .wordmark-sub { font-size: 11px; }

  /* Business card front */
  .card-front { left: 366px; top: 61px; width: 270px; height: 175px; background: var(--paper); border: 1px solid #9a9a9a; }
  .card-name { position: absolute; left: 22px; top: 21px; font-size: 9.5px; font-weight: 700; color: var(--brand); }
  .card-role { position: absolute; left: 22px; top: 34px; font-size: 7.5px; font-weight: 300; color: var(--grey); }
  .card-contacts { position: absolute; left: 22px; top: 59px; list-style: none; font-size: 7.3px; font-weight: 300; color: var(--grey); }
  .card-contacts li { display: flex; align-items: center; gap: 4px; height: 12.4px; }
  .card-contacts svg { width: 7px; height: 7px; flex: none; }
  .card-band { position: absolute; left: 0; right: 0; bottom: 0; height: 58px; background: var(--band); color: #fff; }
  .card-company { position: absolute; left: 22px; top: 18px; font-size: 6.4px; font-weight: 700; }
  .card-address { position: absolute; left: 22px; top: 29px; font-size: 6.4px; font-weight: 300; }
  .card-web { position: absolute; left: 161px; top: 29px; font-size: 6.4px; font-weight: 700; }

  /* Folder */
  .folder { left: 559px; top: 392px; width: 534px; height: 754px; background: var(--band); border: 1px solid #8a1216; }
  .folder .wordmark { position: absolute; left: 0; right: 0; top: 310px; color: #fff; }
  .folder .wordmark-row { font-size: 36px; padding-left: 68px; justify-content: center; }
  .folder .wordmark-sub { font-size: 17px; margin-left: 68px; }

  /* Letterhead */
  .letter { left: 115px; top: 354px; width: 534px; height: 754px; background: var(--paper); border: 1px solid #9a9a9a; }
  .letter .wordmark { position: absolute; left: 386px; top: 60px; width: 110px; color: var(--brand); }
  .letter .wordmark-row { font-size: 17px; }
  .letter .wordmark-sub { font-size: 10px; }
  .sender-line { position: absolute; left: 51px; top: 113px; display: flex; align-items: center; gap: 4px; font-size: 5.4px; font-weight: 300; color: var(--grey); }
  .sender-line i { width: 3px; height: 3px; background: var(--brand); display: block; margin: 0 1px; }
  .fold-mark { position: absolute; left: 0; height: 1px; background: #333; }
  .letter-body { position: absolute; left: 51px; top: 264px; width: 430px; font-size: 8.6px; line-height: 13.4px; font-weight: 300; color: #2a2a2a; }
  .letter-body p + p { margin-top: 13.4px; }
  .letter-body .signature { margin-top: 40px; }
  .letter-footer { position: absolute; left: 0; right: 0; bottom: 0; height: 71px; background: var(--band); color: #fff; font-size: 5.5px; line-height: 10.7px; font-weight: 400; }
  .footer-col { position: absolute; top: 17px; }
</style>
</head>
<body>

  <!-- Business card back -->
  <section class="sheet card-back" aria-label="Visitenkarte Rückseite">
    <div class="wordmark">
      <div class="wordmark-row"><span class="wordmark-square"></span>Fenrokare</div>
      <div class="wordmark-sub">Pflegedienste</div>
    </div>
  </section>

  <!-- Business card front -->
  <section class="sheet card-front" aria-label="Visitenkarte Vorderseite">
    <div class="card-name">Jonas Weller</div>
    <div class="card-role">Geschäftsführer</div>
    <ul class="card-contacts">
      <li>
        <svg viewBox="0 0 10 10"><rect width="10" height="10" fill="#a3161a"/><path d="M2.6 2.2l1.4 1.6-.7.8c.5 1 1.1 1.6 2.1 2.1l.8-.7 1.6 1.4-.7 1c-2.6-.4-4.5-2.3-5-5z" fill="#fff"/></svg>
        0123 45 67 80
      </li>
      <li>
        <svg viewBox="0 0 10 10"><rect width="10" height="10" fill="#a3161a"/><rect x="2" y="4" width="6" height="3.6" fill="#fff"/><rect x="3" y="1.8" width="4" height="2.2" fill="#fff"/><rect x="3" y="5.8" width="4" height="0.7" fill="#a3161a"/></svg>
        0123 45 67 81
      </li>
      <li>
        <svg viewBox="0 0 10 10"><rect width="10" height="10" fill="#a3161a"/><rect x="2" y="3" width="6" height="4.2" fill="#fff"/><path d="M2 3l3 2.4L8 3" fill="none" stroke="#a3161a" stroke-width=".8"/></svg>
        j.weller@fenrokare-pflege.de
      </li>
    </ul>
    <div class="card-band">
      <div class="card-company">Fenrokare Pflegedienst</div>
      <div class="card-address">Lindenweg 42 • 54321 Beispielstadt</div>
      <div class="card-web">www.fenrokare-pflege.de</div>
    </div>
  </section>

  <!-- Folder -->
  <section class="sheet folder" aria-label="Mappe">
    <div class="wordmark">
      <div class="wordmark-row"><span class="wordmark-square"></span>Fenrokare</div>
      <div class="wordmark-sub">Pflegedienste</div>
    </div>
  </section>

  <!-- Letterhead -->
  <section class="sheet letter" aria-label="Briefpapier">
    <div class="wordmark">
      <div class="wordmark-row"><span class="wordmark-square"></span>Fenrokare</div>
      <div class="wordmark-sub">Pflegedienste</div>
    </div>

    <div class="sender-line">
      <span>Fenrokare Pflegedienst</span><i></i><span>Lindenweg 42</span><i></i><span>54321 Beispielstadt</span>
    </div>

    <span class="fold-mark" style="top:266px;width:15px"></span>
    <span class="fold-mark" style="top:376px;width:25px"></span>
    <span class="fold-mark" style="top:533px;width:15px"></span>

    <div class="letter-body">
      <p>Sehr geeherter Herr Weller,</p>
      <p>Nam essenisquas sapere doluptam voluptam, idit et, vent, erferor rorpos reste liberi qui omnis vellupt atibus, omnihiciti quamus untionse necerov itibus cusdanda nihiliquo velitatia aliquidit velis ut od es aut aperum quatemo luptur.</p>
      <p>Am etus dolupta nes molore, te moditatibus, ipsunt porionem re volutem olupta dem qui dellit odit ut eaqui odigenis sed quasit et reptatem inienda provita tiumque et ea quis solum alique viducia non repelit fugia de escid ut ant exeruptis que suntis untionsectia int as quisimpor maionem postiorerum quiae nonse ne simi, consequi ius nonectation cusda quas volupici dis duciis et od etur, acid ut aut officiatusae pa volorrum intibeature, sincipsam venis acipsam quaspero beriorem rempost, que venisit eatiosamusa nobit vellat quati reius.</p>
      <p>Dellore pelitatur? Catem qui im volorerem quodi simint eaquid que quassed maximin venducit qui deliquatum exceperspe am, cuscidi tiossendae ad et eum cum debit, simposs invellu ptatque poriore sequia ditatemposae nis mod quo test, ius vent etur, ommodip suntempor arupta debit estibus cienimus plab illiquis dolupta non pratibe rcidus eaquia incimoluptat quamet hillandamus modis quia velignihilit perum quam liquas eaquam que pore eumqui doluptat.</p>
      <p>Mit&nbsp; freundlichen Grüßen,</p>
      <p class="signature">Jonas Weller</p>
    </div>

    <footer class="letter-footer">
      <div class="footer-col" style="left:51px">fenrokare-pflege<br>Geschäftsführende Gesellschafter:<br>Jonas Weller</div>
      <div class="footer-col" style="left:191px">Hauptverwaltung Beispielstadt<br>Amtsgericht Beispielstadt, HRB123<br>USt-IdNr. DE 1234567890</div>
      <div class="footer-col" style="left:317px">Lindenweg 42<br>54321 Beispielstadt</div>
      <div class="footer-col" style="left:416px">T. 0123 45 67 80<br>F. 0123 45 67 81<br>info@fenrokare-pflege.de</div>
    </footer>
  </section>

</body>
</html>
```